Plover Freightworks Business Card Design

We are a trucking and warehousing company. We run freight in the US manly from the Pacific NW to TX and back up the the PNW. We also do warehousing where we store, move, and distribute freight. Looking for a clean and modern design of business card. We would like to look rich and elegant. Attached is our logo.

Industry/Entity Type

Trucking Company

Contact Information for Business Card

Looking for a clean and modern design of business card. We would like to look rich and elegant.

Font styles to use
Sans Serif

Colors

Designer to choose colors to be used in the design.

Requirements
Must have
• logo but it should not dominate the card
Should not have
• logo should not dominate the card

```html
<!DOCTYPE html>
<html lang="en">
<head>
<meta charset="utf-8">
<title>Plover Freightworks Business Card</title>
<link href="https://fonts.googleapis.com/css2?family=Roboto:wght@400;500;700&display=swap" rel="stylesheet">
<style>
  :root {
    --stage: #1e1e1e;
    --orange: #f7961f;
    --blue: #1784cc;
    --blue-deep: #0f74bd;
    --paper: #f4f4f4;
    --ink-blue: #1f8ad2;
    --white: #ffffff;
  }
  * { margin: 0; padding: 0; box-sizing: border-box; }
  html, body {
    width: 1200px; height: 886px; overflow: hidden;
    background: var(--stage);
    font-family: "Roboto", Arial, sans-serif;
  }
  .sheet {
    width: 1200px; height: 886px;
    display: flex; align-items: center; justify-content: center; gap: 40px;
  }
  .card {
    position: relative; width: 540px; height: 310px; overflow: hidden;
  }
  .card-front {
    background: var(--orange);
    display: flex; align-items: center; justify-content: center;
  }
  .front-name {
    color: var(--white); font-weight: 700; font-size: 30px; letter-spacing: 1px;
    display: flex; align-items: center; gap: 14px;
  }
  .front-name .dot {
    width: 22px; height: 22px; border-radius: 50%; background: var(--white);
  }
  .card-back .shapes { position: absolute; inset: 0; }
  .brand {
    position: absolute; left: 34px; top: 138px;
    display: flex; align-items: center; gap: 10px;
    color: var(--ink-blue); font-weight: 500; font-size: 22px; letter-spacing: .5px;
  }
  .brand .dot { width: 16px; height: 16px; border-radius: 50%; background: var(--ink-blue); }
  .contact {
    position: absolute; left: 352px; top: 56px; color: var(--white);
  }
  .contact .name { font-weight: 700; font-size: 19px; letter-spacing: .5px; }
  .contact .role { font-weight: 500; font-size: 13px; margin-bottom: 18px; }
  .contact .address { font-size: 12px; line-height: 1.35; margin-bottom: 12px; }
  .contact ul { list-style: none; font-size: 12px; }
  .contact li { display: flex; align-items: center; gap: 8px; line-height: 1.45; }
  .contact svg { width: 11px; height: 11px; fill: var(--white); flex: none; }
</style>
</head>
<body>
<main class="sheet">
  <section class="card card-front">
    <div class="front-name"><span class="dot"></span>Plover Freightworks</div>
  </section>

  <section class="card card-back">
    <svg class="shapes" viewBox="0 0 540 310" preserveAspectRatio="none">
      <rect width="540" height="310" fill="var(--blue)"/>
      <path d="M0 0H540V310H0Z" fill="var(--blue-deep)" opacity=".25"/>
      <path d="M0 60C120 10 230 0 270 20C340 70 350 220 330 310H0Z" fill="var(--orange)"/>
      <path d="M0 60C110 20 200 10 250 25C300 80 300 220 265 310H0Z" fill="var(--paper)"/>
    </svg>

    <div class="brand"><span class="dot"></span>Plover Freightworks</div>

    <div class="contact">
      <div class="name">DANIEL REEVE</div>
      <div class="role">CEO/FOUNDER</div>
      <div class="address">4120 Alder Row<br>Anchorage, Alaska 34570</div>
      <ul>
        <li><svg viewBox="0 0 12 12"><path d="M2.5 1l2 2.2-1 1.3c.7 1.5 1.8 2.6 3.3 3.3l1.3-1 2.2 2-1 1.7C5 10.2 1.8 7 1 2z"/></svg>555 214 7730</li>
        <li><svg viewBox="0 0 12 12"><path d="M3 0h6v12H3zM4 1.5v8h4v-8z"/></svg>555 386 1942</li>
        <li><svg viewBox="0 0 12 12"><path d="M3 0h6v3H3zM1 4h10v6H1zM3 8h6v4H3z"/></svg>555 907 4415</li>
        <li><svg viewBox="0 0 12 12"><path d="M0 2h12v1L6 7 0 3zM0 4.5l6 4 6-4V10H0z"/></svg>info@ploverfreightworks.com</li>
      </ul>
    </div>
  </section>
</main>
</body>
</html>
```